Flyer-Design für Rasseclub
sehr angenehme Zusammenarbeit - tolle Vorschläge - Anregungen werden prompt umgesetzt. Vielen Dank für den schönen Flyer. Vom Drucker habe ich auch noch ein Lob erhalten. "Nicht jeder Grafiker / Designer liefere solche gute Qualität ab"
Zielgruppe
Wir sind ein Rasseclub für die Zebu-Züchter in der Schweiz. Wir setzen uns für die Interessen und die Verbreitung der Zeburinder ein. Mit unserem Flyer versuchen wir interessierten Personen einen kurzen Überblick über die Rasse zu verschaffen.
Aufgabenstellung
Wir wünschen uns einen Flyer im A4 Format, welcher 1 oder 2x gefalzt ist. Vorne und hinten Beschriftet / Gestaltet.

```html
<!DOCTYPE html>
<html lang="de">
<head>
<meta charset="utf-8">
<title>Rasseclub Zebu Alpin – Flyer</title>
<link href="https://fonts.googleapis.com/css2?family=Open+Sans:wght@400;600;700&display=swap" rel="stylesheet">
<style>
  :root{
    --olive:#5e6a3b;
    --olive-light:#7d8760;
    --red:#e2202a;
    --stage:#dcdcdc;
    --paper:#ffffff;
    --ink:#222222;
    --grass-top:#d9dcd6;
    --grass:#6f8f3c;
    --grass-deep:#4d7229;
  }
  *{box-sizing:border-box;margin:0;padding:0}
  html,body{width:1200px;height:3905px;overflow:hidden}
  body{background:var(--stage);font-family:"Open Sans",Arial,sans-serif;color:var(--ink);position:relative}
  .sheet{position:absolute;background:var(--paper);overflow:hidden}
  .panel{position:absolute;top:0;bottom:0;overflow:hidden}
  .red-bar{position:absolute;left:0;right:0;bottom:0;height:15px;background:var(--red)}
  .photo{position:absolute;left:0;right:0}
  .photo--bull{background:linear-gradient(180deg,#9fb36a 0%,#86a24a 45%,#7a9a45 80%,#c8b79a 100%)}
  .photo--herd{background:linear-gradient(180deg,#8a9684 0%,#a9b98d 25%,#7fa046 55%,#6d9238 100%)}
  .photo--field{background:linear-gradient(180deg,rgba(255,255,255,1) 0%,var(--grass-top) 18%,#a7ae9c 35%,var(--grass) 60%,var(--grass-deep) 100%)}
  .logo{position:absolute;left:0;right:0;display:flex;align-items:center;justify-content:center;gap:8px;font-weight:700;font-size:17px;letter-spacing:1px;color:var(--ink)}
  .logo-dot{width:10px;height:10px;border-radius:50%;background:var(--red)}
  .title{position:absolute;right:54px;text-align:right;color:#fff}
  .title .sub{font-size:21px;font-weight:400;line-height:1.2}
  .title .main{font-size:26px;font-weight:700;line-height:1.3}
  h2{font-size:15px;font-weight:700;letter-spacing:.2px;padding-bottom:12px;margin-bottom:22px;position:relative}
  h2::after{content:"";position:absolute;left:0;bottom:0;width:235px;height:2px;background:var(--red)}
  p{font-size:10.4px;line-height:1.38;margin-bottom:6px}
  .copy{position:absolute}
  .on-olive{color:#fff}
  .contact-box{position:absolute;background:var(--paper)}
  .contact-box .logo{top:40px}
  .contact-box .label{position:absolute;left:16px;top:118px;font-size:10px}
  .contact-box .strip{position:absolute;left:0;right:0;bottom:0;height:16px;background:var(--olive-light)}
  .divider{position:absolute;top:40px;height:610px;width:1px;background:#888}
</style>
</head>
<body>

<!-- Cover panel -->
<section class="sheet" style="left:436px;top:88px;width:322px;height:677px">
  <div class="logo" style="top:44px"><span class="logo-dot"></span>ALPIN ZEBU</div>
  <div class="photo photo--bull" style="top:118px;height:392px" role="img" aria-label="Foto eines braunen Zebu-Stiers auf einer Weide"></div>
  <div style="position:absolute;left:0;right:0;top:510px;height:152px;background:var(--olive)">
    <div style="height:12px;background:var(--olive-light)"></div>
  </div>
  <div class="title" style="top:560px;right:56px"><div class="sub">Rasseclub</div><div class="main">ZEBU ALPIN</div></div>
  <div class="red-bar"></div>
</section>

<!-- Outside spread -->
<section class="sheet" style="left:120px;top:845px;width:956px;height:678px">
  <div class="panel" style="left:0;width:312px">
    <div class="photo photo--herd" style="top:0;height:352px" role="img" aria-label="Foto einer Zebu-Herde mit Kälbern auf der Weide"></div>
    <div class="copy" style="left:35px;top:400px;width:240px">
      <h2>HERKUNFT</h2>
      <p>Die Zebus (Bos indicus) gehören zu den Buckelrindern, die sich nicht nur vom Erbgut, sondern auch vom äusseren Erscheinungsbild her stark von den anderen Rinderrassen in Europa unterscheiden. Die Zebus stammen ursprünglich aus Sri Lanka und dem südlichen Kaukasus. Heute sind sie auf der ganzen Welt verbreitet. Die Zeburasse wird in 600 Rasseschläge unterteilt: vom kleinsten Zwergzebu bis zu den grössten Brahma oder Nelore. Das Wort Zebu wird vom tibetanischen Wort „zeu“ respektive „zeba“ abgeleitet, welches übersetzt Buckel heisst.</p>
    </div>
  </div>
  <div class="panel" style="left:312px;width:322px;background:var(--olive)">
    <div class="copy on-olive" style="left:32px;top:56px;width:252px">
      <h2>RASSECLUB</h2>
      <p>Bei «Herdenbund Schweiz» sind über 150 Muttertiere der Rasse Zwergzebu und Zebu registriert. Der «Rasseclub Zebu Alpin» gibt es seit dem Jahr 2015. Alle, die Zebus in der Schweiz halten, sind im Rasseclub herzlich willkommen. Die Tiere können, wie jedes andere Rind auch, bei «Herdenbund Schweiz» angemeldet werden. Selbstverständlich können auch die anerkannten Stiere im Herdebuch von «Herdenbund Schweiz» aufgenommen werden und sind somit als Zuchtstiere anerkannt.</p>
    </div>
    <div class="contact-box" style="left:32px;top:333px;width:252px;height:290px">
      <div class="logo"><span class="logo-dot"></span>ALPIN ZEBU</div>
      <div class="label">Ihr Zebuhalter in der Nähe:</div>
      <div class="strip"></div>
    </div>
  </div>
  <div class="panel" style="left:634px;width:322px">
    <div class="logo" style="top:44px"><span class="logo-dot"></span>ALPIN ZEBU</div>
    <div class="photo photo--bull" style="top:118px;height:392px" role="img" aria-label="Foto eines braunen Zebu-Stiers auf einer Weide"></div>
    <div style="position:absolute;left:0;right:0;top:510px;bottom:0;background:var(--olive)"><div style="height:12px;background:var(--olive-light)"></div></div>
    <div class="title" style="top:560px;right:56px"><div class="sub">Rasseclub</div><div class="main">ZEBU ALPIN</div></div>
  </div>
  <div class="red-bar"></div>
</section>

<!-- Inside spread -->
<section class="sheet" style="left:120px;top:1588px;width:956px;height:676px">
  <div class="photo photo--field" style="top:150px;bottom:0" role="img" aria-label="Foto einer Reihe brauner Zebus am Heu im Nebel auf einer grünen Wiese"></div>
  <div class="divider" style="left:322px"></div>
  <div class="divider" style="left:642px"></div>
  <div class="copy" style="left:40px;top:48px;width:260px">
    <h2 style="margin-bottom:14px">MERKMALE UND EIGENSCHAFTEN</h2>
    <p>Der Buckel ist das auffälligste, äussere Merkmal der Zeburinder. Das ausgesprochen marmorierte Buckelfleisch ist eine Delikatesse. Das übrige Muskelfleisch ist sehr fettarm, mit einem leichten Wildgeschmack, feinfaserig und enthält die gesunden Omega-3-Fettsäuren.</p>
    <p>Zum typischen Erscheinungsbild der Zebus gehören neben dem Buckel die Hörner, eine starke Wamme, ein abgezogenes und stark abgedachtes Becken, feine Extremitäten und eine schmale Stirn, die dem Kopf eine längliche Form verleiht.</p>
  </div>
  <div class="copy" style="left:357px;top:48px;width:260px">
    <p>Die Grösse der Tiere kann stark variieren. Die Kühe sind deutlich kleiner als die Stiere. Zebus kommen in allen Farben und Farbkombinationen vor. Auch die Hörner sind nicht immer klassisch nach oben gerichtet.</p>
    <p>Zebus sind sehr robust und gehören zu den extensiven Rinderrassen. Die Klauenpflege kann auf ein Minimum beschränkt werden. Die Tiere sind betreffend Futter sehr genügsam. Ihnen reicht im Sommer Gras und im Winter Heu. Auf Kraftfutter und andere Zusätze, mit Ausnahme von Salz, kann verzichtet werden. Die Abkalbung ist meist leicht und geschieht ohne menschliche Hilfe. Die Mutterkühe haben einen guten Schutzinstinkt für ihre Kälber.</p>
  </div>
  <div class="copy" style="left:672px;top:48px;width:260px">
    <p>Während die meisten europäischen Rinderrassen unter der Sommerhitze leiden, fühlen sich Zebus bei Temperaturen um 30 Grad noch wohl. Ihr schütteres Fell und die dicke Aussenhaut schützen sie vor der Hitze. In den letzten Jahren wurde beobachtet, dass Zebusperma auch bei Temperaturen über 38°C noch befruchtungsfähig bleibt. Kalte Temperaturen sind sie sich von ihrer Heimat auch gewohnt.</p>
    <h2 style="margin-top:28px;margin-bottom:16px">EINSATZ</h2>
    <p>Durch ihr leichtes Gewicht verursachen Zebus kaum Trittschäden, wodurch sie fast überall einsetzbar sind. Sie können auch gut zur allgemeinen Landschaftspflege eingesetzt werden.</p>
  </div>
  <div class="red-bar"></div>
</section>

<!-- Partly folded view, shown flat -->
<section class="sheet" style="left:275px;top:2380px;width:645px;height:676px">
  <div class="panel" style="left:0;width:355px">
    <div class="photo photo--field" style="top:200px;bottom:0" role="img" aria-label="Foto brauner Zebus am Heu im Nebel auf einer grünen Wiese"></div>
    <div class="copy" style="left:40px;top:46px;width:262px">
      <h2 style="margin-bottom:14px">MERKMALE UND EIGENSCHAFTEN</h2>
      <p>Der Buckel ist das auffälligste, äussere Merkmal der Zeburinder. Das ausgesprochen marmorierte Buckelfleisch ist eine Delikatesse. Das übrige Muskelfleisch ist sehr fettarm, mit einem leichten Wildgeschmack, feinfaserig und enthält die gesunden Omega-3-Fettsäuren.</p>
      <p>Zum typischen Erscheinungsbild der Zebus gehören neben dem Buckel die Hörner, eine starke Wamme, ein abgezogenes und stark abgedachtes Becken, feine Extremitäten und eine schmale Stirn, die dem Kopf eine längliche Form verleiht.</p>
    </div>
  </div>
  <div class="panel" style="left:355px;width:290px">
    <div class="photo photo--herd" style="top:0;height:345px" role="img" aria-label="Foto einer Zebu-Herde mit Kälbern auf der Weide"></div>
    <div style="position:absolute;left:0;right:0;top:345px;height:12px;background:var(--olive-light)"></div>
    <div class="copy" style="left:28px;top:392px;width:240px">
      <h2>HERKUNFT</h2>
      <p>Die Zebus (Bos indicus) gehören zu den Buckelrindern, die sich nicht nur vom Erbgut, sondern auch vom äusseren Erscheinungsbild her stark von den anderen Rinderrassen in Europa unterscheiden. Die Zebus stammen ursprünglich aus Sri Lanka und dem südlichen Kaukasus. Heute sind sie auf der ganzen Welt verbreitet. Die Zeburasse wird in 600 Rasseschläge unterteilt: vom kleinsten Zwergzebu bis zu den grössten Brahma oder Nelore. Das Wort Zebu wird vom tibetanischen Wort „zeu“ respektive „zeba“ abgeleitet, welches übersetzt Buckel heisst.</p>
    </div>
  </div>
  <div class="red-bar"></div>
</section>

<!-- Back panel -->
<section class="sheet" style="left:436px;top:3115px;width:322px;height:675px;background:var(--olive)">
  <div class="copy on-olive" style="left:32px;top:56px;width:258px">
    <h2>RASSECLUB</h2>
    <p>Bei «Herdenbund Schweiz» sind über 150 Muttertiere der Rasse Zwergzebu und Zebu registriert. Der «Rasseclub Zebu Alpin» gibt es seit dem Jahr 2015. Alle, die Zebus in der Schweiz halten, sind im Rasseclub herzlich willkommen. Die Tiere können, wie jedes andere Rind auch, bei «Herdenbund Schweiz» angemeldet werden. Selbstverständlich können auch die anerkannten Stiere im Herdebuch von «Herdenbund Schweiz» aufgenommen werden und sind somit als Zuchtstiere anerkannt.</p>
  </div>
  <div class="contact-box" style="left:38px;top:332px;width:252px;height:290px">
    <div class="logo"><span class="logo-dot"></span>ALPIN ZEBU</div>
    <div class="label">Ihr Zebuhalter in der Nähe:</div>
    <div class="strip"></div>
  </div>
  <div class="red-bar"></div>
</section>

</body>
</html>
```